Commercial Auto Insurance Application and Commercial Property Insurance Application

Hi I need a fillable application for my business to send to potential clients for Commercial Auto Insurance and Commercial Property Insurance. I have attached an example application I currently use for another line of insurance.
Commercial Auto Insurance Application
On the first page I would need the following:
- Business Name: (fill in area for text)
- Effective Date: (fill in area for text)
- How do you structure your business? (Check box for “Sole Proprietor”, “Partnership”, “Corporation”, “LLC”)
- Contact Name: (fill in area for text) / Phone Number: (fill in area for text) / Contact Email (fill in area for text)
- Mailing address: (fill in area for text)
- Garaging location: (fill in area for text)
- Owner Name: (fill in area for text)
- Description of Operations: (fill in area for text)
- How long has the operation been in business? (fill in area for text)
- How many years of experience does your management have in the truck/transportation industry? (fill in area for text)
Coverages
Liability Combined Single Limit: ($1,000,000 (checkbox) / $500,000 (checkbox / $300,000 (checkbox) / Other: (fill in area for text)
Uninsured Motorist CSL: (fill in area for text) (checkbox for “Rejected”)
Medical Payments: (fill in area for text)
Physical Damage: (fill in area for text) (checkbox for Rejected)
Liability Deducible: ($500 checkbox, $1,000 checkbox, $2,500 checkbox, $5,000 checkbox)
Physical Damage Deductible: ($500 checkbox, $1,000 checkbox, $2,500 checkbox, $5,000 checkbox)
Driving radius: (fill in area for text)
How many years have you had your own continuous commercial auto insurance coverage for the current business name? (fill in area for text)
Do any of your vehicles travel across state lines? Yes (checkbox)/ No (checkbox)
If yes, please list all states in which vehicles operate: (fill in area for text)
What is the maximum radius traveled for your customer's business?
0-25 miles (checkbox)
26-50 miles (checkbox)
51-75 miles (checkbox)
76-100 miles (checkbox)
101-150 miles (checkbox)
151-200 miles (checkbox)
201-300 miles (checkbox)
300+ miles (checkbox)
Would you like physical damage coverage for this vehicle? (should be for each vehicle listed)
On the 2nd page of the application I would need the following:
I would need to have it where people can fill in the vehicle information such as VIN:, Year:, Make:, Model:, Type of Vehicle:, Trailers:, Value:
I would also need to have it where people can fill in the drivers with their driver info including Name:, DOB:, DL #:, DL State:, Class of License:, Married: Yes/No, Number of years driving similar vehicle:
Please make it where you can fill in 20 vehicle's information and 20 driver's info.
For the 2nd Application I would need one for Property Insurance
On the Commercial Property Application I would need the following:
- Building Address: (fill in area for text)
- Building Description: (fill in area for text)
- Building Amount: $(fill in area for text)
- Business Personal Property Amount: $ (fill in area for text) (checkbox for Not Needed)
- Building Sq Ft: (fill in area for text)
- Total Area Sq Ft: (fill in area for text)
- Building Construction Type: Wood Frame (checkbox), Steel (checkbox), Fire Resistive (checkbox), Non-Combustible (checkbox), Other (fill in area for text)
- # of stories: (fill in area for text)
- Year Built: (fill in area for text)
- Wiring improvement year: (fill in area for text)
- Roofing improvement year: (fill in area for text)
- Plumbing improvement year: (fill in area for text)
- Heating improvement year: (fill in area for text)
- What is to the right of the building and distance: (fill in area for text)
- What is to the left of the building and distance: (fill in area for text)
- What is in front of the building and distance: (fill in area for text)
- What is behind the building and distance: (fill in area for text)
- Burglar alarm installation and serviced by: (fill in area for text) None (checkbox)
- Does the premises have fire protection? Sprinkler system (checkbox), Fire detection (checkbox), Other: (fill in area for text) None (checkbox)

```html
<!DOCTYPE html>
<html lang="en">
<head>
<meta charset="utf-8">
<title>Commercial Auto Insurance Application</title>
<link href="https://fonts.googleapis.com/css2?family=Archivo+Black&family=Arimo:wght@400;700&display=swap" rel="stylesheet">
<style>
  :root {
    --brand-blue: #29a9e1;
    --field-white: #ffffff;
    --ink: #1a1a1a;
    --backdrop: #b4b4b4;
  }
  html, body {
    margin: 0;
    padding: 0;
    width: 1199px;
    height: 1200px;
    overflow: hidden;
    background: var(--backdrop);
  }
  .stage {
    position: relative;
    width: 1199px;
    height: 1200px;
    overflow: hidden;
  }
  .application {
    position: absolute;
    left: 149px;
    top: 16px;
    width: 663px;
    height: 858px;
    background: var(--brand-blue);
    transform: scale(1.36);
    transform-origin: 0 0;
    font-family: "Arimo", Arial, sans-serif;
    font-size: 10px;
    color: var(--ink);
  }
  .application > * { position: absolute; box-sizing: border-box; }
  .form-title {
    top: 14px; left: 0; width: 663px;
    text-align: center;
    font-family: "Archivo Black", "Arial Black", sans-serif;
    font-size: 20px;
    line-height: 26px;
    color: var(--field-white);
    margin: 0;
    letter-spacing: 0.2px;
  }
  .section-title {
    left: 30px; top: 347px;
    font-family: "Archivo Black", "Arial Black", sans-serif;
    font-size: 20px;
    line-height: 24px;
    color: var(--field-white);
    margin: 0;
  }
  .field {
    background: var(--field-white);
    padding-left: 15px;
    line-height: 21px;
    height: 21px;
    white-space: nowrap;
  }
  .field.tall { line-height: 12px; padding-top: 6px; }
  .field.full { left: 15px; width: 633px; }
  .field.centered { padding-left: 0; text-align: center; }
  .field-sub { position: absolute; top: 0; }
  .option-label {
    color: var(--field-white);
    line-height: 21px;
    height: 21px;
    white-space: nowrap;
  }
  .checkbox {
    width: 24px; height: 21px;
    border: 1.2px solid var(--field-white);
  }
  .checkbox.dark { border-color: #222; height: 22px; width: 23px; }
  .radius-option { line-height: 14px; white-space: nowrap; }
  .footnote {
    left: 30px; top: 811px;
    color: var(--field-white);
    line-height: 14px;
    white-space: nowrap;
  }
</style>
</head>
<body>
<div class="stage">
  <section class="application">
    <h1 class="form-title">COMMERCIAL AUTO INSURANCE APPLICATION</h1>

    <div class="field full" style="top:50px">Business Name:<span class="field-sub" style="left:405px">Effective Date:</span></div>
    <div class="field full" style="top:75px">How do you structure your business?</div>

    <span class="option-label" style="top:100px;left:30px">Sole Proprietor</span>
    <span class="checkbox" style="top:100px;left:110px"></span>
    <span class="option-label" style="top:100px;left:147px">Partnership</span>
    <span class="checkbox" style="top:100px;left:218px"></span>
    <span class="option-label" style="top:100px;left:264px">Corporation</span>
    <span class="checkbox" style="top:100px;left:329px"></span>
    <span class="option-label" style="top:100px;left:381px">LLC</span>
    <span class="checkbox" style="top:100px;left:432px"></span>

    <div class="field" style="top:125px;left:15px;width:197px">Contact Name:</div>
    <div class="field" style="top:125px;left:219px;width:181px">Phone Number:</div>
    <div class="field" style="top:125px;left:406px;width:242px">Contact Email:</div>

    <div class="field full" style="top:149px">Mailing address:</div>
    <div class="field full" style="top:174px">Garaging location:</div>
    <div class="field full" style="top:199px">Owner Name:</div>
    <div class="field full tall" style="top:224px;height:50px">Description of Operations:</div>
    <div class="field full tall" style="top:277px;height:43px">How long has the operation been in business?</div>
    <div class="field full" style="top:324px">How many years of experience does your management have in the truck/transportation industry?</div>

    <h2 class="section-title">COVERAGES</h2>

    <div class="field full" style="top:370px">Liability Combined Single Limit:</div>
    <span class="option-label" style="top:395px;left:30px">$1,000,000</span>
    <span class="checkbox" style="top:395px;left:99px"></span>
    <span class="option-label" style="top:395px;left:147px">$500,000</span>
    <span class="checkbox" style="top:395px;left:210px"></span>
    <span class="option-label" style="top:395px;left:264px">$300,000</span>
    <span class="checkbox" style="top:395px;left:322px"></span>
    <span class="option-label" style="top:395px;left:381px">Other:</span>
    <div class="field" style="top:395px;left:418px;width:230px"></div>

    <div class="field" style="top:420px;left:15px;width:350px">Uninsured Motorist CSL:</div>
    <div class="field" style="top:420px;left:370px;width:120px;padding-left:11px">Rejected</div>
    <div class="field full" style="top:445px">Medical Payments:</div>
    <div class="field" style="top:470px;left:15px;width:350px">Physical Damage:</div>
    <div class="field centered" style="top:470px;left:370px;width:120px">Rejected</div>

    <div class="field full" style="top:495px">Liability Deducible:</div>
    <span class="option-label" style="top:520px;left:59px">$500</span>
    <span class="checkbox" style="top:520px;left:99px"></span>
    <span class="option-label" style="top:520px;left:147px">$1,000</span>
    <span class="checkbox" style="top:520px;left:210px"></span>
    <span class="option-label" style="top:520px;left:264px">$2,500</span>
    <span class="checkbox" style="top:520px;left:322px"></span>
    <span class="option-label" style="top:520px;left:381px">$5,000</span>
    <div class="field" style="top:520px;left:418px;width:230px"></div>

    <div class="field full" style="top:545px">Physical Damage Deductible:</div>
    <span class="option-label" style="top:570px;left:59px">$500</span>
    <span class="checkbox" style="top:570px;left:99px"></span>
    <span class="option-label" style="top:570px;left:147px">$1,000</span>
    <span class="checkbox" style="top:570px;left:210px"></span>
    <span class="option-label" style="top:570px;left:264px">$2,500</span>
    <span class="checkbox" style="top:570px;left:322px"></span>
    <span class="option-label" style="top:570px;left:381px">$5,000</span>

    <div class="field full" style="top:607px">Driving radius:</div>
    <div class="field full tall" style="top:632px;height:46px">How many years have you had your own continuous commercial auto insurance coverage for the current business name?</div>
    <div class="field full" style="top:682px">Do any of your vehicles travel across state lines?<span class="field-sub" style="left:248px">Yes</span><span class="field-sub" style="left:327px">No</span></div>
    <div class="field full" style="top:707px">If yes, please list all states in which vehicles operate:</div>

    <div class="field full tall" style="top:732px;height:72px">What is the maximum radius traveled for your customer's business?</div>
    <span class="radius-option" style="top:760px;left:30px">0-25 miles</span>
    <span class="checkbox dark" style="top:756px;left:81px"></span>
    <span class="radius-option" style="top:760px;left:107px">26-50 miles</span>
    <span class="checkbox dark" style="top:756px;left:160px"></span>
    <span class="radius-option" style="top:760px;left:186px">51-75 miles</span>
    <span class="checkbox dark" style="top:756px;left:237px"></span>
    <span class="radius-option" style="top:760px;left:264px">76-100 miles</span>
    <span class="checkbox dark" style="top:756px;left:339px"></span>
    <span class="radius-option" style="top:760px;left:381px">101-150 miles</span>
    <span class="checkbox dark" style="top:756px;left:451px"></span>
    <span class="radius-option" style="top:785px;left:30px">151-200 miles</span>
    <span class="checkbox dark" style="top:780px;left:109px"></span>
    <span class="radius-option" style="top:785px;left:147px">201-300 miles</span>
    <span class="checkbox dark" style="top:780px;left:218px"></span>
    <span class="radius-option" style="top:785px;left:264px">300+ miles</span>
    <span class="checkbox dark" style="top:780px;left:317px"></span>

    <p class="footnote" style="margin:0">Would you like physical damage coverage for this vehicle? (should be for each vehicle listed)</p>
  </section>
</div>
</body>
</html>
```